Business card for a "family office" company

Please provide professional looking business card designs, incorporating the attached logo and below details. Harrowmere Holdings Pty Ltd is a family office / financial investment company. We are looking for a modern, professional and contemporary card design.

Industry/Entity Type

Finance

Contact Information for Business Card

Name: Dean Mollick
Title: Director
Company: Harrowmere Holdings Pty Ltd
Email: harrowdean@quillnet.example
Mobile: 0462 735 418
Address: 4/312 Barnaby Parade, Wrenfield QLD 4573, Australia

Requirements
Must have
• All details above and the logo. logo only on back side. incorporate colours of logo
Nice to have
• up to you
Should not have
• ?

```html
<!DOCTYPE html>
<html lang="en">
<head>
<meta charset="utf-8">
<title>Harrowmere Holdings – Business Cards</title>
<link rel="stylesheet" href="https://fonts.googleapis.com/css2?family=Open+Sans:wght@400;600;700&display=swap">
<style>
  :root {
    --stage: #0c0c0c;
    --cream: #f8f6f1;
    --navy: #23215a;
    --royal: #2b3a94;
    --ink: #1d1b4f;
    --white: #ffffff;
  }
  * { box-sizing: border-box; margin: 0; padding: 0; }
  html, body {
    width: 1200px; height: 1000px; overflow: hidden;
    background: var(--stage);
    font-family: "Open Sans", sans-serif;
  }
  .canvas { position: relative; width: 1200px; height: 1000px; }
  .card {
    position: absolute; width: 560px; height: 320px;
    border-radius: 16px; overflow: hidden;
    background: var(--cream);
    box-shadow: 0 10px 30px rgba(0,0,0,.6);
  }
  .card__waves { position: absolute; inset: 0; width: 100%; height: 100%; }
  .card--back { left: 60px; top: 150px; }
  .card--front { left: 580px; top: 510px; }

  .brand {
    position: absolute; left: 56px; top: 150px;
    display: flex; align-items: center; gap: 12px;
    color: var(--navy); font-weight: 600; font-size: 26px; letter-spacing: .5px;
    line-height: 1.15;
  }
  .brand__mark { width: 18px; height: 18px; background: var(--navy); flex: none; }

  .front-name {
    position: absolute; left: 40px; top: 70px;
    color: var(--navy); font-weight: 600; font-size: 22px; line-height: 1.15;
  }

  .contact { position: absolute; left: 300px; top: 62px; color: var(--ink); }
  .contact__name { font-weight: 700; font-size: 21px; color: var(--navy); line-height: 1.1; }
  .contact__title { font-size: 16px; margin-bottom: 14px; }
  .contact__list { list-style: none; font-size: 13.5px; font-weight: 600; }
  .contact__item { display: flex; align-items: center; gap: 8px; margin-bottom: 3px; }
  .contact__icon { width: 13px; height: 13px; flex: none; }

  .address {
    position: absolute; left: 40px; bottom: 30px;
    color: var(--white); font-size: 14px;
  }
</style>
</head>
<body>
<main class="canvas">

  <section class="card card--back" aria-label="Card back">
    <svg class="card__waves" viewBox="0 0 560 320" preserveAspectRatio="none" aria-hidden="true">
      <path d="M0,0 H560 V230 C470,215 400,175 330,110 C260,50 150,40 0,95 Z" fill="var(--navy)"/>
      <path d="M0,95 C150,40 260,50 330,110 C400,175 470,215 560,230 L560,240 C470,228 395,188 325,124 C255,62 150,55 0,108 Z" fill="var(--royal)"/>
      <path d="M0,104 C150,50 258,59 327,118 C397,183 470,222 560,235" fill="none" stroke="var(--white)" stroke-width="2"/>
    </svg>
    <div class="brand">
      <span class="brand__mark"></span>
      <span>Harrowmere<br>Holdings</span>
    </div>
  </section>

  <section class="card card--front" aria-label="Card front">
    <svg class="card__waves" viewBox="0 0 560 320" preserveAspectRatio="none" aria-hidden="true">
      <path d="M0,150 C120,140 230,160 300,230 C360,285 450,290 560,250 V320 H0 Z" fill="var(--navy)"/>
      <path d="M0,135 C120,124 235,146 305,214 C365,270 450,278 560,238 L560,252 C450,292 360,287 300,232 C230,162 120,142 0,152 Z" fill="var(--royal)"/>
      <path d="M0,146 C120,135 232,156 302,224 C362,279 450,285 560,246" fill="none" stroke="var(--white)" stroke-width="2"/>
    </svg>

    <div class="front-name">Harrowmere<br>Holdings</div>

    <div class="contact">
      <p class="contact__name">Dean Mollick</p>
      <p class="contact__title">Director</p>
      <ul class="contact__list">
        <li class="contact__item">
          <svg class="contact__icon" viewBox="0 0 14 14" aria-hidden="true"><rect x="3.5" y="1" width="7" height="12" rx="1.2" fill="none" stroke="var(--ink)" stroke-width="1.4"/><circle cx="7" cy="11" r=".8" fill="var(--ink)"/></svg>
          <span>0462 735 418</span>
        </li>
        <li class="contact__item">
          <svg class="contact__icon" viewBox="0 0 14 14" aria-hidden="true"><rect x="1" y="3" width="12" height="8" fill="var(--ink)"/><path d="M1,3 L7,8 L13,3" fill="none" stroke="var(--cream)" stroke-width="1"/></svg>
          <span>harrowdean@quillnet.example</span>
        </li>
        <li class="contact__item">
          <svg class="contact__icon" viewBox="0 0 14 14" aria-hidden="true"><g fill="none" stroke="var(--ink)" stroke-width="1.2"><circle cx="7" cy="7" r="5.8"/><ellipse cx="7" cy="7" rx="2.6" ry="5.8"/><path d="M1.2,7 H12.8 M2,4 H12 M2,10 H12"/></g></svg>
          <span>www.quillnet.example</span>
        </li>
      </ul>
    </div>

    <p class="address">4/312 Barnaby Parade, Wrenfield QLD 4573, Australia</p>
  </section>

</main>
</body>
</html>
```